TAVRO Capital Group LLC a High Risk Big Rewards company for Rich Young Entrepreneurs

We would like a very modern, powerful in the eyes of our customers, modern, minimalist feel, financial gain. this business card is for young Rich entrepreneurs who want to invest money into High Risk, Big Rewards Businesses. The card Should sell the business!! let your creativity go Wild! I pick most of the designers for this project because of your BOLD Designs, I would like this card to be Bold, Modern, Minimalist, use as many effects in your graphic Artist Mind, Do not let the Financial sound of this business to make you think Conservative that's the last thing we are! if you have a lot of money and you want to play a risky market call US
Updates

Project Deadline Extended
Reason: have not received, enough designs to choose 1st and second place, sure I have received over 100 designs but it seems most designers are submitting every card they have ever made before and calling it mine, please we are looking for fresh ideas please!

Target Market(s)

Private Risky Investors

Industry/Entity Type

Financial

Contact Information for Business Card

powerful in the eyes of our customers,modern, minimalist feel

Font styles to use
Other font styles liked:
• Modern feeling fonts

Requirements
Must have
• The Company Name is TAVRO Capital Group LLC and it must be on the CARD
• My Name, title, Cell , email
• Delvin Ashcroft G.E.D.
• Managing Member
• 555.038.6195
• delvin@tavrocapitalgroup.example
Nice to have
• try a black thick plastic card with round corners with Delvin Ashcroft GED (make sure GED is smaller than name) just on one side of the card, and my phone number with out the icons and email on the other side, this card should look like a exclusive credit card or exclusive VIP card, something you would never loose

```html
<!DOCTYPE html>
<html lang="en">
<head>
<meta charset="utf-8">
<title>TAVRO Capital Group LLC — Business Card</title>
<link rel="stylesheet" href="https://fonts.googleapis.com/css2?family=Montserrat:wght@400;500;700&family=Open+Sans:ital,wght@1,400&display=swap">
<style>
  :root {
    --page: #e4e2df;
    --ink: #111111;
    --paper: #ffffff;
    --panel: #d6d6d6;
    --panel-light: #f1f1f1;
    --rule: #555555;
  }
  * { box-sizing: border-box; margin: 0; padding: 0; }
  html, body {
    width: 1200px; height: 900px; overflow: hidden;
    background: var(--page);
    font-family: "Montserrat", sans-serif;
  }
  .canvas {
    width: 1200px; height: 900px;
    display: flex; flex-direction: column; align-items: center; justify-content: center;
    gap: 36px;
  }
  .card {
    position: relative;
    width: 700px; height: 400px;
    box-shadow: 0 10px 30px rgba(0,0,0,0.18);
    overflow: hidden;
  }

  /* Brand side */
  .card--brand { background: var(--paper); }
  .card--brand .band {
    position: absolute; top: 0; bottom: 0; left: 27%; width: 46%;
    background: var(--ink);
  }
  .brand {
    position: absolute; display: flex; align-items: center; gap: 16px;
  }
  .brand__dot {
    flex: none; border-radius: 50%; border-style: solid;
  }
  .brand__name {
    font-weight: 700; text-transform: uppercase; letter-spacing: 0.02em; line-height: 1.1;
  }
  .card--brand .brand {
    left: 27%; width: 46%; top: 0; bottom: 0; justify-content: center;
  }
  .card--brand .brand__dot { width: 58px; height: 58px; border-width: 3px; border-color: var(--paper); }
  .card--brand .brand__name { color: var(--paper); font-size: 27px; }

  /* Details side */
  .card--details { background: var(--ink); }
  .details__frame {
    position: absolute; inset: 18px;
    border: 4px solid var(--paper);
    background: linear-gradient(135deg, #cfcfcf 0%, var(--panel) 50%, #e6e6e6 100%);
  }
  .details__center {
    position: absolute; top: 0; bottom: 0; left: 36%; width: 27%;
    background: var(--panel-light);
  }
  .rule { position: absolute; background: var(--rule); }
  .rule--top { left: 6%; right: 6%; top: 30%; height: 1px; }
  .rule--bottom { left: 6%; right: 6%; bottom: 14%; height: 1px; }
  .rule--divider { left: 56%; top: 44%; height: 26%; width: 1px; }
  .card--details .brand {
    left: 0; right: 0; top: 8%; justify-content: center; gap: 12px;
  }
  .card--details .brand__dot { width: 44px; height: 44px; border-width: 3px; border-color: var(--ink); }
  .card--details .brand__name { color: var(--ink); font-size: 19px; }
  .person {
    position: absolute; right: 46%; top: 50%; text-align: right; color: var(--ink);
  }
  .person__name { font-size: 22px; font-weight: 500; }
  .person__name small { font-size: 15px; }
  .person__title {
    font-family: "Open Sans", sans-serif; font-style: italic; font-size: 15px; color: #333; margin-top: 4px;
  }
  .contact {
    position: absolute; left: 58%; top: 47%; color: var(--ink);
    font-size: 14px; line-height: 2; font-weight: 400;
  }
</style>
</head>
<body>
<main class="canvas">
  <section class="card card--brand" aria-label="Business card, brand side">
    <div class="band"></div>
    <div class="brand">
      <span class="brand__dot"></span>
      <span class="brand__name">TAVRO Capital<br>Group LLC</span>
    </div>
  </section>

  <section class="card card--details" aria-label="Business card, contact side">
    <div class="details__frame">
      <div class="details__center"></div>
      <div class="rule rule--top"></div>
      <div class="rule rule--bottom"></div>
      <div class="rule rule--divider"></div>
      <div class="brand">
        <span class="brand__dot"></span>
        <span class="brand__name">TAVRO Capital<br>Group LLC</span>
      </div>
      <div class="person">
        <p class="person__name">Delvin Ashcroft <small>G.E.D.</small></p>
        <p class="person__title">Managing Member</p>
      </div>
      <div class="contact">
        <p>555.038.6195</p>
        <p>delvin@tavrocapitalgroup.example</p>
      </div>
    </div>
  </section>
</main>
</body>
</html>
```